Wayline Billboard Co Business Card Design

We have a newly created business and logo, but we now need business cards using the new logo.
We are an Australian based business, and we sell advertising space on trucks. The business cards will be seen by media buyers, direct advertisers, fleet owners and business people in general.
Our colours are very simple - black and a strong yellow, with some white. We have chosen the black and yellow for various reasons, but in particular because they are high contrast, and they also have a parallel with the number plates used on our roads, which is relevant to our product offering.
My initial thoughts:
Keep it simple and uncluttered
Use both sides
Our default is Century Gothic
I can provide logo files as required. We do not yet have a website, so I can't direct you there just yet. That may well be another project!
Target Market(s)
The business cards will be seen by media buyers, direct advertisers, fleet owners and business people in general.
Industry/Entity Type
Advertising
Look and feel
Each slider illustrates characteristics of the customer's brand and the style your logo design should communicate.

```html
<!DOCTYPE html>
<html lang="en">
<head>
<meta charset="utf-8">
<title>Wayline Billboard Co — Business Card</title>
<link rel="stylesheet" href="https://fonts.googleapis.com/css2?family=Questrial&display=swap">
<style>
  :root {
    --backdrop: #b3b4b6;
    --card-black: #000000;
    --brand-yellow: #f2e21b;
    --card-radius: 19px;
  }
  * { margin: 0; padding: 0; box-sizing: border-box; }
  html, body {
    width: 1200px;
    height: 429px;
    overflow: hidden;
    background: var(--backdrop);
  }
  body {
    position: relative;
    font-family: "Questrial", "Century Gothic", sans-serif;
    color: var(--brand-yellow);
  }
  .card {
    position: absolute;
    top: 78px;
    width: 486px;
    height: 279px;
    background: var(--card-black);
    border-radius: var(--card-radius);
    overflow: hidden;
  }
  .card--front { left: 99px; }
  .card--back { left: 636px; }

  .website {
    position: absolute;
    left: 40px;
    top: 150px;
    font-size: 21px;
    letter-spacing: 4px;
  }
  .brand {
    position: absolute;
    left: 300px;
    top: 112px;
    display: flex;
    align-items: flex-start;
    gap: 12px;
  }
  .brand__square {
    width: 34px;
    height: 34px;
    background: var(--brand-yellow);
    flex: none;
  }
  .brand__name {
    font-size: 24px;
    line-height: 1.2;
    letter-spacing: 1px;
  }

  .details {
    position: absolute;
    right: 39px;
    top: 34px;
    text-align: right;
  }
  .details__name {
    font-size: 23px;
    font-weight: 700;
    line-height: 1;
  }
  .details__role {
    font-size: 18px;
    letter-spacing: 1px;
    margin-top: 4px;
  }
  .details__address {
    margin-top: 28px;
    font-size: 15px;
    line-height: 19px;
  }
  .details__contact {
    margin-top: 30px;
    font-size: 15px;
    line-height: 19px;
  }
  .details__label { font-weight: 700; }
</style>
</head>
<body>
  <section class="card card--front">
    <p class="website">wayline.com.au</p>
    <div class="brand">
      <span class="brand__square"></span>
      <p class="brand__name">Wayline<br>Billboard Co</p>
    </div>
  </section>

  <section class="card card--back">
    <div class="details">
      <p class="details__name">Dean Harlow</p>
      <p class="details__role">Founder</p>
      <p class="details__address">
        Wayline Billboard Co<br>
        PO Box 2417<br>
        Harbourview NSW 2091
      </p>
      <p class="details__contact">
        <span class="details__label">P:</span> 1800WAYLINE<br>
        <span class="details__label">M:</span> +61 4 2851 7302<br>
        <span class="details__label">E:</span> dean@wayline.com.au
      </p>
    </div>
  </section>
</body>
</html>
```